Re-design of professional audio retail website brevlando.co.nz

Our current website brevlando.co.nz is now 20 years old and needs a refresh. All our customers love the easy navigation style so we would like to keep a similar style of top navigation bar and the drop down Products, Categories, sub categories etc, menu on the left that stays there on all pages except the front page. For each category page the right hand pane is to have icons for the sub categories like our current site
So in essence all the same functionality and similar layout of the old website but just smartened up to make it look more modern.
We like the the darker blue background colours in the old website and would like it to have some kind of subtle audio/sound theme to it like the waveforms used in the old one.
We would like the main front landing page designed, plus the sub categories icons page including the style of left side category/sub category navigation. Plus some ideas for a product page.
Main front page to have similar components to current website. ie Content carousel, browse categories, brands, some specials/new products
If you've submitted a logo to our other design request then feel free to use that on this design as we’ve not chosen the winner from that yet. If you’ve not designed a logo then use our existing one

Target Market(s)

Musicians, schools, churches, theatres, DJ's

Industry/Entity Type

Professional audio, sound systems, DJ gear.

Font styles to use
Sans Serif

Colors

Designer to choose colors to be used in the design.

Requirements
Must have
• Product images on white background. Search engine field at top right always visible. Drop down left side navigation/filtering bar that is there all the time once off the main index page. Darker blue background. Top menu bar with tabs for Products (that drops down to categories), Special Offers, Brands, Discounts, About Us, Contact Us.
Nice to have
• A tech or audio feel to it, some subtle reference to audio waveforms in the backgroundmaybe

```html
<!DOCTYPE html>
<html lang="en">
<head>
<meta charset="utf-8">
<title>Brevlando NZ — Microphones</title>
<link href="https://fonts.googleapis.com/css2?family=Inter:wght@400;500;600;700;800&display=swap" rel="stylesheet">
<style>
:root{
  --navy-deep:#0b1a2e;
  --navy:#12294a;
  --navy-panel:#15305a;
  --nav-band:#0d1c33;
  --sky:#3fc6f2;
  --page-light:#eef2f8;
  --panel:#f4f6f9;
  --card:#ffffff;
  --ink:#0f1b2d;
  --muted:#5b6778;
  --link:#1e5fa8;
  --line:#dde4ee;
  --side-text:#dbe6f5;
}
*{box-sizing:border-box;margin:0;padding:0}
html,body{width:1200px;height:1111px;overflow:hidden}
body{font-family:"Inter",sans-serif;background:var(--page-light);position:relative;color:var(--ink)}
.backdrop{position:absolute;left:0;top:0;width:1200px;height:525px;background:radial-gradient(ellipse at 10% 10%,#163a5c 0%,var(--navy) 40%,var(--navy-deep) 100%)}
.trust-strip{position:absolute;right:131px;top:9px;display:flex;gap:14px;font-size:9.4px;color:#e4ecf7;font-weight:500}
.site-header{position:absolute;left:131px;top:27px;width:938px;height:120px;border:1px solid #244268;border-radius:6px;background:linear-gradient(90deg,#0f2748,#153563);overflow:hidden}
.brand{position:absolute;left:14px;top:44px;display:flex;align-items:center;gap:6px;color:#fff;font-weight:700;font-size:14px;letter-spacing:.5px}
.brand-dot{width:8px;height:8px;border-radius:50%;background:var(--sky)}
.search{position:absolute;left:518px;top:24px;display:flex;height:35px}
.search-field{width:333px;border:1px solid #3a5b86;border-right:none;border-radius:4px 0 0 4px;background:#0e2240;color:#dfe8f4;font-size:12.5px;display:flex;align-items:center;padding-left:11px}
.search-btn{width:73px;background:var(--sky);border-radius:0 4px 4px 0;color:#0b1a2e;font-weight:700;font-size:12.5px;display:flex;align-items:center;justify-content:center}
.main-nav{position:absolute;left:0;bottom:0;width:100%;height:37px;background:var(--nav-band);display:flex;align-items:center;padding-left:14px;gap:30px}
.main-nav a{color:#fff;text-decoration:none;font-weight:800;font-size:11px}
.sidebar{position:absolute;left:131px;top:164px;width:212px;height:468px;background:var(--navy-panel);border:1px solid #25467a;border-radius:5px;padding:14px 14px 0;box-shadow:0 10px 24px rgba(10,25,50,.25)}
.sidebar-title{color:#fff;font-weight:700;font-size:14px;padding-bottom:11px;border-bottom:1px solid #2c4c7a}
.cat{border-bottom:1px solid #2c4c7a;padding:8px 0 4px}
.cat:last-child{border-bottom:none}
.cat-head{color:#fff;font-weight:700;font-size:12.5px;display:flex;align-items:center;gap:5px;height:16px}
.cat-head svg{width:8px;height:8px;fill:#fff}
.cat ul{list-style:none;margin-top:5px}
.cat li{height:32px;display:flex;align-items:center;padding-left:8px;color:var(--side-text);font-size:10.6px}
.cat li.active{background:var(--sky);color:#0b1a2e;border-radius:3px;height:26px;margin-bottom:6px}
.cat.closed{padding:8px 0 7px}
.content{position:absolute;left:360px;top:164px;width:709px;height:822px;background:var(--panel);border-radius:5px}
.crumbs{position:absolute;left:22px;top:23px;font-size:10px;font-weight:600;color:var(--muted)}
.crumbs a{color:var(--link);text-decoration:none}
.crumbs span{margin:0 5px;color:#9aa5b4}
.eyebrow{position:absolute;left:22px;top:61px;font-size:9px;font-weight:700;letter-spacing:1.3px;color:var(--sky)}
.page-title{position:absolute;left:21px;top:73px;font-size:37px;font-weight:700;color:var(--ink);letter-spacing:-.3px}
.intro{position:absolute;left:358px;top:63px;width:310px;font-size:12.5px;line-height:19.5px;color:var(--muted)}
.toolbar{position:absolute;left:22px;top:130px;width:664px;height:48px;border:1px solid var(--line);border-radius:4px;background:#f1f4f8;display:flex;align-items:center;justify-content:space-between;padding:0 11px}
.toolbar-count{font-size:12.5px;color:var(--muted)}
.sort{display:flex;align-items:center;gap:7px;font-size:12.5px;color:var(--muted);font-weight:600}
.sort-select{background:#fff;border:1px solid var(--line);border-radius:4px;padding:5px 4px;color:var(--ink);font-weight:700;display:flex;align-items:center;gap:4px}
.grid{position:absolute;left:22px;top:192px;display:grid;grid-template-columns:repeat(3,213px);grid-auto-rows:194px;gap:13px 13px}
.card{background:var(--card);border:1px solid var(--line);border-radius:4px;padding:15px 15px 0;position:relative}
.thumb{width:69px;height:69px;border:1px solid var(--line);border-radius:4px;display:flex;align-items:center;justify-content:center;background:#fff}
.thumb div{width:46px;height:46px;border-radius:4px}
.card h3{position:absolute;left:15px;top:95px;font-size:12.5px;font-weight:600;color:var(--ink)}
.card p{position:absolute;left:15px;top:116px;width:185px;font-size:10px;line-height:15px;color:var(--muted)}
.card .count{position:absolute;left:15px;top:165px;font-size:10px;font-weight:700;color:var(--link)}
.site-footer{position:absolute;left:131px;top:1003px;width:938px;height:86px;background:var(--navy-deep);border-radius:5px}
.footer-brand{position:absolute;left:20px;top:28px;display:flex;align-items:center;gap:6px;color:#fff;font-weight:700;font-size:12px}
.footer-info{position:absolute;left:216px;top:25px;color:#fff}
.footer-info strong{display:block;font-size:12.5px;font-weight:700}
.footer-info span{display:block;font-size:12.5px;color:#c3d2e6;margin-top:4px}
.footer-links{position:absolute;right:18px;top:34px;display:flex;gap:13px}
.footer-links a{color:#fff;font-weight:700;font-size:12.5px;text-decoration:none}
</style>
</head>
<body>
<div class="backdrop"></div>

<div class="trust-strip">
  <span>NZ pro-audio authorised retailer</span>
  <span>Official NZ warranties</span>
  <span>Schools, churches, venues &amp; installers</span>
</div>

<header class="site-header">
  <div class="brand"><span class="brand-dot"></span>Brevlando</div>
  <div class="search">
    <div class="search-field">Search microphones, speakers, DJ gear...</div>
    <div class="search-btn">Search</div>
  </div>
  <nav class="main-nav">
    <a href="#">PRODUCTS</a>
    <a href="#">SPECIAL OFFERS</a>
    <a href="#">BRANDS</a>
    <a href="#">DISCOUNTS</a>
    <a href="#">ABOUT US</a>
    <a href="#">CONTACT US</a>
  </nav>
</header>

<aside class="sidebar">
  <div class="sidebar-title">Products</div>
  <div class="cat">
    <div class="cat-head"><svg viewBox="0 0 10 10"><path d="M0 1h10L5 9z"/></svg>Microphones</div>
    <ul>
      <li class="active">Wireless Microphones</li>
      <li>Wired Vocal Microphones</li>
      <li>USB &amp; Podcast Mics</li>
      <li>Instrument Mics</li>
      <li>Lavalier &amp; Headsets</li>
    </ul>
  </div>
  <div class="cat">
    <div class="cat-head"><svg viewBox="0 0 10 10"><path d="M0 1h10L5 9z"/></svg>Speakers</div>
    <ul>
      <li>Powered Speakers</li>
      <li>Passive Speakers</li>
      <li>Subwoofers</li>
      <li>Install Speakers</li>
    </ul>
  </div>
  <div class="cat closed">
    <div class="cat-head"><svg viewBox="0 0 10 10"><path d="M1 0v10l8-5z"/></svg>DJ Gear</div>
  </div>
  <div class="cat closed">
    <div class="cat-head"><svg viewBox="0 0 10 10"><path d="M1 0v10l8-5z"/></svg>Install &amp; Accessories</div>
  </div>
</aside>

<main class="content">
  <div class="crumbs"><a href="#">Home</a><span>/</span><a href="#">Products</a><span>/</span>Microphones</div>
  <div class="eyebrow">CATEGORY</div>
  <h1 class="page-title">Microphones</h1>
  <p class="intro">Choose a microphone subcategory, then refine by brand, application or stock status.</p>

  <div class="toolbar">
    <span class="toolbar-count">Showing 8 subcategories</span>
    <div class="sort">Sort <span class="sort-select">Most popular <svg width="8" height="6" viewBox="0 0 8 6"><path d="M1 1l3 3 3-3" stroke="#0f1b2d" stroke-width="1.4" fill="none"/></svg></span></div>
  </div>

  <div class="grid">
    <article class="card">
      <div class="thumb"><div role="img" aria-label="Product photo of a wireless microphone" style="background:linear-gradient(160deg,#d8d2c4,#8a8376)"></div></div>
      <h3>Wireless Microphones</h3>
      <p>Handheld, headset and lavalier systems for venues and schools.</p>
      <span class="count">42 products</span>
    </article>
    <article class="card">
      <div class="thumb"><div role="img" aria-label="Product photo of a vocal microphone" style="background:linear-gradient(160deg,#d8d2c4,#8a8376)"></div></div>
      <h3>Wired Vocal Microphones</h3>
      <p>Road-ready dynamic mics for singers, speech and rehearsal rooms.</p>
      <span class="count">31 products</span>
    </article>
    <article class="card">
      <div class="thumb"><div role="img" aria-label="Product photo of desktop studio speakers" style="background:linear-gradient(160deg,#5a5d62,#222427)"></div></div>
      <h3>USB &amp; Podcast Mics</h3>
      <p>Simple computer-ready recording for creators and workspaces.</p>
      <span class="count">18 products</span>
    </article>
    <article class="card">
      <div class="thumb"><div role="img" aria-label="Product photo of a portable recorder" style="background:linear-gradient(160deg,#6b5a4a,#252525)"></div></div>
      <h3>Studio Condensers</h3>
      <p>Large and small diaphragm mics for studio tracking.</p>
      <span class="count">27 products</span>
    </article>
    <article class="card">
      <div class="thumb"><div role="img" aria-label="Product photo of a guitar amplifier" style="background:linear-gradient(160deg,#5b4636,#1f1a17)"></div></div>
      <h3>Instrument Mics</h3>
      <p>Drum, guitar, brass and acoustic instrument solutions.</p>
      <span class="count">24 products</span>
    </article>
    <article class="card">
      <div class="thumb"><div role="img" aria-label="Product photo of a vocal effects pedal" style="background:linear-gradient(160deg,#6f7780,#2a2f35)"></div></div>
      <h3>Vocal Effects</h3>
      <p>Processors, pitch tools and vocal performance accessories.</p>
      <span class="count">12 products</span>
    </article>
    <article class="card">
      <div class="thumb"><div role="img" aria-label="Product photo of microphone cables and accessories" style="background:linear-gradient(160deg,#4a6fa8,#1c2230)"></div></div>
      <h3>Mic Cables &amp; Accessories</h3>
      <p>XLR leads, clips, shock mounts, windscreens and adaptors.</p>
      <span class="count">96 products</span>
    </article>
    <article class="card">
      <div class="thumb"><div role="img" aria-label="Product photo of microphone stands" style="background:linear-gradient(160deg,#e6e8eb,#8d9299)"></div></div>
      <h3>Mic Stands</h3>
      <p>Boom stands, desk arms and stage stand hardware.</p>
      <span class="count">35 products</span>
    </article>
  </div>
</main>

<footer class="site-footer">
  <div class="footer-brand"><span class="brand-dot"></span>Brevlando</div>
  <div class="footer-info">
    <strong>Brevlando NZ</strong>
    <span>Professional audio category browsing concept.</span>
  </div>
  <nav class="footer-links">
    <a href="#">Home</a>
    <a href="#">Products</a>
    <a href="#">Product</a>
  </nav>
</footer>
</body>
</html>
```